Plakat-Design für ein großes, geistliches Konzert für Chor, Orchester und Solisten
Zielgruppe
Wir sind eine Kantorei einer Kirchengemeinde, die in jedem Jahr ein großes Konzert für Chor, Orchester und Solisten veranstaltet. In diesem Jahr ist das Konzert in doppeltem Sinn etwas Besonderes. Zum einen weil wir das Konzert in Kooperation mit einer anderen Kantorei bestreiten und zum anderen weil die Anzahl der Mitwirkenden so groß ist, dass wir nicht der Kirche sondern das Konzert in die hiesige Stadthalle verlagern. Die Kirchenmusik präsentiert sozusagen sich außerhalb ihrer eigenen Mauern.
Eine Zielgruppe sollen diejenigen sein, die sich durch den besoneren Veranstaltungsort ansprechen lassen, also eher kirchenfremde Menschen. Das Plakat sollte auch das bestehende Stammpublikum nicht abschrecken, sondern einladen.
Es ist ein Folgeauftrag geplant, und zwar ein Programmheft/Textheft für das Konzert mit dem gleichen Design als Grundlage.
Aufgabenstellung
Das Plakat soll im DIN A3 oder A4 Hochformat erstellt werden.
Zwei weitere Logos von Förderern folgen noch.
Außer der Turm sind alle Logos von Förderern.
Der Turm ist sozusagen unser Markenzeichen und ein Wiedererkennungsmerkmal.
Das Konzert steht unter dem Motto: Von der Finsternis zum Licht.
Bezüglich der Textgröße sollte dieses Motto nicht größer sein als z.B. der Komponist und das Werk. Vielmehr soll das Motto durch ein grafisches Element eingearbeitet werden. 'Brautigorff' und 'Sternruf' sollen Eye catcher-Worte sein. Sternruf ist der Titel des Konzertes!

```html
<!DOCTYPE html>
<html lang="de">
<head>
<meta charset="utf-8">
<title>Sternruf – Konzertplakat</title>
<link rel="stylesheet" href="https://fonts.googleapis.com/css2?family=Oswald:wght@300;400;500;600&display=swap">
<style>
  :root {
    --stage: #a7a6a8;
    --magenta: #a8237f;
    --violet: #7a4a9a;
    --teal: #1f9ba8;
    --deep: #0b3a44;
    --night: #081216;
    --mint: #74c9b9;
    --white: #ffffff;
    --ink-dark: #143540;
    --footer-mint: #d5ecea;
    --footer-ink: #333333;
    --footer-accent: #8a2f6a;
  }
  * { margin: 0; padding: 0; box-sizing: border-box; }
  html, body { width: 1200px; height: 1200px; overflow: hidden; background: var(--stage); }
  body { position: relative; font-family: "Oswald", "Arial Narrow", sans-serif; }

  .poster {
    position: absolute;
    left: 176px; top: 0;
    width: 1057px; height: 1497px;
    transform: scale(0.8016);
    transform-origin: 0 0;
    overflow: hidden;
    background:
      radial-gradient(ellipse 70% 45% at 90% 85%, var(--night) 0%, rgba(8,18,22,0.85) 40%, rgba(8,18,22,0) 80%),
      linear-gradient(180deg, var(--magenta) 0%, #9a2f86 12%, var(--violet) 24%, #3fa0b4 40%, var(--teal) 50%, var(--deep) 72%, #0c2a32 100%);
  }
  .poster > * { position: absolute; white-space: nowrap; line-height: 1; }

  .staff-swoosh {
    left: 300px; top: 40px; width: 760px; height: 760px;
    background: radial-gradient(ellipse 60% 25% at 60% 50%, rgba(170,220,230,0.22), rgba(170,220,230,0) 70%);
    transform: rotate(-28deg);
  }
  .portrait {
    left: 680px; top: 400px; width: 377px; height: 640px;
    background: radial-gradient(ellipse 60% 55% at 50% 45%, rgba(40,160,180,0.55), rgba(10,50,60,0.3) 60%, rgba(8,18,22,0) 90%);
  }

  .composer { left: 58px; top: 40px; color: var(--mint); font-weight: 400; }
  .composer .given, .composer .suffix { font-size: 38px; }
  .composer .family { font-size: 80px; font-weight: 500; color: var(--white); letter-spacing: -1px; }

  .cantata { left: 58px; top: 130px; font-size: 46px; font-weight: 400; color: var(--mint); letter-spacing: -0.5px; }

  .work-title { left: 58px; top: 172px; font-size: 120px; font-weight: 500; color: var(--white); letter-spacing: -1px; }
  .work-kind { left: 540px; top: 199px; font-size: 35px; font-weight: 400; color: var(--white); }
  .work-opus { left: 540px; top: 237px; font-size: 52px; font-weight: 400; color: var(--white); }

  .motto { color: var(--ink-dark); }
  .motto-quote-open { left: 50px; top: 377px; font-size: 120px; font-weight: 600; }
  .motto-from { left: 115px; top: 420px; font-size: 68px; font-weight: 400; }
  .motto-dark { left: 185px; top: 493px; font-size: 80px; font-weight: 500; }
  .motto-to { left: 345px; top: 462px; font-size: 30px; font-weight: 400; color: var(--white); }
  .motto-light { left: 397px; top: 431px; font-size: 58px; font-weight: 400; color: var(--white); }
  .motto-quote-close { left: 498px; top: 410px; font-size: 120px; font-weight: 600; color: var(--white); }

  .date { left: 110px; width: 220px; text-align: center; color: var(--mint); font-weight: 400; }
  .date-weekday { top: 807px; font-size: 56px; letter-spacing: 2px; }
  .date-day { top: 846px; font-size: 175px; font-weight: 500; color: var(--white); letter-spacing: -5px; transform: scaleY(1.3); transform-origin: 50% 0; }
  .date-month { top: 1077px; font-size: 52px; }
  .date-time { top: 1137px; font-size: 52px; }
  .date-venue { top: 1200px; font-size: 48px; }
  .date-city { top: 1248px; font-size: 48px; font-weight: 500; }

  .credits { line-height: 1.5; }
  .credits dt { font-size: 9px; font-weight: 500; color: var(--white); text-transform: uppercase; margin-top: 9px; letter-spacing: 0.3px; }
  .credits dd { font-size: 19px; font-weight: 400; color: var(--mint); }
  .credits-cast { left: 570px; top: 818px; }
  .credits-info { left: 810px; top: 990px; }

  .sponsor-band {
    left: 0; top: 1360px; width: 1057px; height: 137px;
    background: linear-gradient(90deg, var(--footer-mint) 0%, var(--footer-mint) 45%, var(--white) 45%);
  }
  .sponsor { top: 1418px; font-size: 18px; font-weight: 400; color: var(--footer-ink); display: flex; align-items: center; gap: 8px; }
  .sponsor .mark { width: 10px; height: 10px; background: var(--footer-accent); border-radius: 50%; }
  .sponsor-church { left: 330px; color: var(--footer-accent); }
  .sponsor-foundation { left: 615px; font-size: 22px; top: 1414px; }
  .sponsor-friends { left: 870px; }
</style>
</head>
<body>
  <main class="poster">
    <div class="staff-swoosh" role="img" aria-label="Geschwungene Notenlinien mit Noten als Hintergrundelement"></div>
    <div class="portrait" role="img" aria-label="Gestochenes Porträt des Komponisten"></div>

    <h1 class="composer"><span class="given">Anselm </span><span class="family">Brautigorff</span><span class="suffix">-Kestrath</span></h1>
    <p class="cantata">Choralkantate „Wer nur den lieben Gott lässt walten”</p>
    <h2 class="work-title">STERNRUF</h2>
    <p class="work-kind">SINFONIE</p>
    <p class="work-opus">OP. 52</p>

    <span class="motto motto-quote-open">„</span>
    <span class="motto motto-from">Von der</span>
    <span class="motto motto-dark">Finsternis</span>
    <span class="motto motto-to">zum</span>
    <span class="motto motto-light">Licht</span>
    <span class="motto motto-quote-close">”</span>

    <p class="date date-weekday">SONNTAG</p>
    <p class="date date-day">22.</p>
    <p class="date date-month">SEPT. 2019</p>
    <p class="date date-time">18.00 UHR</p>
    <p class="date date-venue">STADTHALLE</p>
    <p class="date date-city">BRUNNHAGEN</p>

    <dl class="credits credits-cast">
      <dt>Sopran</dt>
      <dd>Mira Talborn und<br>Lena-Marie Hollweg</dd>
      <dt>Tenor</dt>
      <dd>Jonas Edvik</dd>
      <dt>Überschrift</dt>
      <dd>Kammersinfonie Lindental<br>Kirchenkreiskantorei Eschwalde<br>Kantorei St. Veit, Brunnhagen</dd>
      <dt>Gesamtleitung</dt>
      <dd>Kirchenkreiskantoren<br>Tobias Reinholt (ESW)<br>und Simon Albrecht (BRH)</dd>
    </dl>

    <dl class="credits credits-info">
      <dt>Einlass</dt>
      <dd>17.00 Uhr</dd>
      <dt>Eintrittspreise</dt>
      <dd>25,- / 20,- / 15,- / 10,- Euro<br>(Ermäßigungen 50%)</dd>
      <dt>Kartenvorverkauf</dt>
      <dd>Kulturverein Brunnhagen,<br>Lindenstraße 7, 29999 BRH<br>www.kulturverein-brunnhagen.de</dd>
      <dt>Weitere Informationen</dt>
      <dd>www.stveit-brunnhagen.de<br>www.stadthalle-brunnhagen.de</dd>
    </dl>

    <div class="sponsor-band"></div>
    <p class="sponsor sponsor-church"><span class="mark"></span>Kirchenkreis Brunnhagen</p>
    <p class="sponsor sponsor-foundation">Kreisstiftung Brunnhagen</p>
    <p class="sponsor sponsor-friends">Freundeskreis Chormusik</p>
  </main>
</body>
</html>
```